Parent company of several different entertainment businesses needs urgent business card design

We need a business card design for key senior staff. The company name is "Harborlight Leisure", with full legal name being Harborlight Leisure Group Pte Ltd. No logo is required, just an update to existing design (which is a bit bland). Need to use a similar script font as the "Harborlight" in attached. The "Leisure" can be on a second line if required, with emphasis on the "Harborlight". Will need to make a quick decision within 24hrs.
We operate in Asia, and Australia/NZ. Brands we work with include (www.springvaultco.com.au and www.quillsparkarena.com and www.gripnrise.com). We will need to depict these brand logos on the back of the card. Require artwork file in eps so as can change names etc for additional staff. Thanks
Updates

Target Market(s)

Corporate target (This is the parent company, not the super fun entertainment outlets)

Industry/Entity Type

Business

Contact Information for Business Card

Name: Darren Pellworth
Title: Executive Director
Email: darren@harborlight-leisure.com
Phone: +65 9471 6528
Address: 14 Kelvane Rd, #05-03 Marlow Parkview Plaza, Singapore 248315

Requirements
Should not have
• No picture logo required. Just use the company name, with emphasis on "Harborlight"

```html
<!DOCTYPE html>
<html lang="en">
<head>
<meta charset="utf-8">
<title>Harborlight Leisure – Business Card</title>
<link href="https://fonts.googleapis.com/css2?family=Kaushan+Script&family=Dancing+Script:wght@700&family=Raleway:wght@300&family=Open+Sans:wght@400;600;700&display=swap" rel="stylesheet">
<style>
  :root{
    --page:#d9d9db;
    --ink:#2b2b2b;
    --ink-soft:#4a4a4a;
    --black:#0c0c0c;
    --card:#f4f4f4;
    --card-shade:#e4e4e5;
    --white:#ffffff;
    --brand-blue:#2fa6d9;
    --brand-purple:#6a3aa6;
  }
  *{box-sizing:border-box;margin:0;padding:0}
  html,body{width:1200px;height:904px;overflow:hidden}
  body{background:var(--page);font-family:"Open Sans",sans-serif;color:var(--ink);position:relative}

  .card{position:absolute;left:250px;width:700px;height:400px;overflow:hidden;
    box-shadow:0 6px 18px rgba(0,0,0,.18)}
  .card--back{top:40px;background:linear-gradient(180deg,var(--card),var(--card-shade))}
  .card--front{top:464px;background:linear-gradient(160deg,var(--white),var(--card-shade))}

  .wordmark{position:absolute;left:0;right:0;text-align:center;line-height:1}
  .wordmark__script{display:block;font-family:"Kaushan Script","Dancing Script","Brush Script MT",cursive;
    font-size:62px;font-weight:400;line-height:1.05}
  .wordmark__sub{display:block;font-family:"Raleway",sans-serif;font-weight:300;font-size:24px;
    letter-spacing:7px;margin-top:4px;padding-left:110px}

  .card--back .band{position:absolute;left:0;top:0;width:100%;height:250px;background:var(--black)}
  .card--back .wordmark{top:80px;color:var(--white)}

  .partners{position:absolute;left:0;right:0;top:295px;display:flex;justify-content:center;gap:90px;align-items:center}
  .partner{display:flex;align-items:center;gap:8px;font-weight:700;font-size:19px}
  .partner__dot{width:14px;height:14px;border-radius:50%}
  .partner--quill{color:var(--ink)}
  .partner--quill .partner__dot{background:var(--brand-blue)}
  .partner--grip{color:var(--brand-purple)}
  .partner--grip .partner__dot{background:var(--brand-purple)}

  .card--front .wordmark{top:40px;color:var(--ink)}
  .person{position:absolute;left:0;right:0;top:180px}
  .person__row{display:flex;align-items:center;height:28px}
  .person__name{font-weight:700;font-size:18px;margin-left:auto;padding:0 14px}
  .person__title{font-size:14px;color:var(--ink-soft);padding:0 14px;margin-right:auto}
  .rule{height:1.5px;background:var(--ink)}
  .rule--right{flex:0 0 262px}
  .rule--left{flex:0 0 272px}

  .contact{position:absolute;left:0;right:0;top:268px;text-align:center;font-size:14.5px;line-height:1.55;color:var(--ink)}
  .contact__company{font-weight:700}
  .contact__line{display:flex;justify-content:center;align-items:center;gap:6px}
  .contact__line svg{width:14px;height:14px}
</style>
</head>
<body>

<section class="card card--back" aria-label="Card back">
  <div class="band"></div>
  <div class="wordmark">
    <span class="wordmark__script">Harborlight</span>
    <span class="wordmark__sub">Leisure</span>
  </div>
  <div class="partners">
    <div class="partner partner--quill"><span class="partner__dot"></span>QuillSpark Arena</div>
    <div class="partner partner--grip"><span class="partner__dot"></span>Grip n Rise</div>
  </div>
</section>

<section class="card card--front" aria-label="Card front">
  <div class="wordmark">
    <span class="wordmark__script">Harborlight</span>
    <span class="wordmark__sub">Leisure</span>
  </div>
  <div class="person">
    <div class="person__row">
      <span class="person__name">Darren Pellworth</span>
      <span class="rule rule--right"></span>
    </div>
    <div class="person__row">
      <span class="rule rule--left"></span>
      <span class="person__title">Executive Director</span>
    </div>
  </div>
  <div class="contact">
    <div class="contact__company">Harborlight Leisure Group Pte Ltd</div>
    <div class="contact__line">
      <svg viewBox="0 0 24 24" aria-hidden="true"><path d="M6.6 10.8a15.1 15.1 0 0 0 6.6 6.6l2.2-2.2a1 1 0 0 1 1-.25 11.4 11.4 0 0 0 3.6.57 1 1 0 0 1 1 1V20a1 1 0 0 1-1 1A17 17 0 0 1 3 4a1 1 0 0 1 1-1h3.5a1 1 0 0 1 1 1c0 1.25.2 2.45.57 3.6a1 1 0 0 1-.25 1z" fill="currentColor"/></svg>
      <span>+65 9471 6528 &nbsp;|</span>
      <svg viewBox="0 0 24 24" aria-hidden="true"><rect x="2" y="5" width="20" height="14" rx="2" fill="currentColor"/><path d="M3 6l9 7 9-7" stroke="#fff" stroke-width="1.6" fill="none"/></svg>
      <span>darren@harborlight-leisure.com</span>
    </div>
    <div>14 Kelvane Rd, #05-03 Marlow Parkview Plaza | Singapore 248315</div>
  </div>
</section>

</body>
</html>
```